Redesign MuseQuill's Artist Profile Page

MuseQuill is a contemporary arts website that has a large worldwide community of artists with profile pages for each artist showing artwork, exhibits, bio data, etc.

For an example please see: http://www.musequill-example.com/global/artists/show/47302-dorian-pell

We would like a slight redesign on these pages within the context of the current website. We are interested in modernizing and lightening the design. The artwork should be the primary focus.

Target Market(s)

Professional artists, galleries and collectors

Industry/Entity Type

Artists

Requirements
Must have
• All the current functionality on the page.

```html
<!DOCTYPE html>
<html lang="en">
<head>
<meta charset="utf-8">
<title>Dorian Pell – Artist Profile – MuseQuill</title>
<link rel="stylesheet" href="https://fonts.googleapis.com/css2?family=Open+Sans:wght@400;600&display=swap">
<style>
:root{
  --ink:#3a3a3a;
  --muted:#555;
  --green:#8db61f;
  --header:#555555;
  --sidebar:#ececec;
  --rule:#d9d9d9;
  --dropdown:#b3b3b3;
  --stage:#333333;
  --white:#ffffff;
}
*{box-sizing:border-box;margin:0;padding:0}
html,body{width:1126px;height:1200px;overflow:hidden;background:var(--white)}
body{font-family:"Open Sans",sans-serif;color:var(--ink)}
.page{position:relative;width:1000px;height:1066px;transform:scale(1.126);transform-origin:0 0}
.abs{position:absolute}
a{color:inherit;text-decoration:none}

/* sidebar */
.sidebar{position:absolute;left:0;top:0;width:270px;height:965px;background:var(--sidebar)}
.brand{position:absolute;left:18px;top:28px;width:227px;height:62px;background:var(--white);box-shadow:0 5px 6px rgba(0,0,0,.25);display:flex;align-items:center;justify-content:center;font-size:36px;font-weight:600;color:#555;letter-spacing:-1px}
.main-menu{list-style:none;position:absolute;left:28px;top:137px}
.main-menu li{height:31px;display:flex;align-items:center;font-size:16px;color:#444}
.main-menu li svg{margin-right:20px}
.main-menu li.is-active{color:var(--green)}
.submenu{list-style:none;position:absolute;left:162px;top:160px;width:141px;height:156px;background:var(--dropdown);padding:0 12px 0 17px}
.submenu li{height:31px;line-height:31px;font-size:12.5px;color:#222;border-bottom:1px solid #e5e5e5;letter-spacing:.3px}
.submenu li:last-child{border-bottom:none}
.submenu li.is-hover{color:var(--white)}
.side-title{position:absolute;left:0;width:240px;text-align:center;color:var(--green);font-size:17px}
.side-rule{position:absolute;left:0;width:270px;height:4px;background:linear-gradient(#dcdcdc,#f5f5f5)}
.actions{list-style:none;position:absolute;left:34px;top:501px}
.actions li{height:31px;display:flex;align-items:center;font-size:13px;color:#444}
.actions li svg{margin-right:11px}
.news{list-style:none;position:absolute;left:38px;top:839px;width:200px}
.news li{font-size:11px;line-height:15px;color:#444;margin-bottom:16px}

/* header */
.topbar{position:absolute;left:270px;top:0;width:730px;height:95px;background:var(--header);color:var(--white)}
.country{position:absolute;left:332px;top:8px;font-size:13px}
.select{position:absolute;left:393px;top:6px;width:126px;height:22px;background:#aaa;font-size:13px;padding-left:13px;line-height:22px}
.select .caret{position:absolute;right:0;top:0;width:24px;height:22px;background:#888}
.userlinks{position:absolute;top:9px;font-size:13px;color:#ddd}
.tabs{position:absolute;left:22px;top:69px;display:flex;gap:17px;font-size:13px;list-style:none}
.tabs li.is-current{color:var(--green)}
.search-label{position:absolute;left:504px;top:66px;font-size:13px}
.search-box{position:absolute;left:563px;top:64px;width:154px;height:24px;background:var(--white)}

/* slideshow */
.stage{position:absolute;left:310px;top:125px;width:640px;height:395px;background:var(--stage)}
.stage .photo{position:absolute;left:153px;top:9px;width:334px;height:350px;background:linear-gradient(150deg,#3b2a22 0%,#1e1613 45%,#b48a6e 75%,#8f7a70 100%)}
.stage .caption{position:absolute;left:0;right:0;top:363px;text-align:center;color:var(--white);font-size:16px}
.stage .ctrl{position:absolute;top:364px}
.thumbs{position:absolute;left:330px;top:528px;display:flex;gap:12px}
.thumb{width:76px;height:76px;border:3px solid var(--white);box-shadow:0 1px 4px rgba(0,0,0,.4)}

/* content */
.section-title{position:absolute;left:309px;color:var(--green);font-size:17px;font-weight:400}
.facts{position:absolute;left:358px;top:657px;font-size:14px;color:#444;border-collapse:collapse}
.facts td{height:29px;vertical-align:middle}
.facts .key{width:94px;font-size:13.5px}
.facts .sep{width:16px}
.statement{position:absolute;left:340px;top:829px;width:593px;font-size:14px;line-height:19px;text-align:justify;color:#444}

/* footer */
.footer{position:absolute;left:0;top:965px;width:1000px;height:101px;background:var(--header);color:var(--white)}
.footer-links{position:absolute;top:29px;left:0;right:0;text-align:center;font-size:11.5px;word-spacing:0}
.footer-links span{margin:0 19px}
.copyright{position:absolute;top:59px;left:0;right:0;text-align:center;font-size:11px;padding-left:4px}
</style>
</head>
<body>
<div class="page">

  <aside class="sidebar">
    <div class="brand">MuseQuill</div>

    <ul class="main-menu">
      <li><svg width="12" height="12"><circle cx="6" cy="6" r="5.5" fill="#fff" stroke="#999"/><path d="M5 3.5 8 6 5 8.5z" fill="#666"/></svg>HOME</li>
      <li class="is-active"><svg width="12" height="12"><circle cx="6" cy="6" r="5.5" fill="#fff" stroke="#999"/><path d="M5 3.5 8 6 5 8.5z" fill="#666"/></svg>MAGAZINE</li>
      <li><svg width="12" height="12"><circle cx="6" cy="6" r="5.5" fill="#fff" stroke="#999"/><path d="M5 3.5 8 6 5 8.5z" fill="#666"/></svg>CALENDAR</li>
      <li><svg width="12" height="12"><circle cx="6" cy="6" r="5.5" fill="#fff" stroke="#999"/><path d="M5 3.5 8 6 5 8.5z" fill="#666"/></svg>GALLERIES</li>
      <li><svg width="12" height="12"><circle cx="6" cy="6" r="5.5" fill="#fff" stroke="#999"/><path d="M5 3.5 8 6 5 8.5z" fill="#666"/></svg>ART</li>
      <li><svg width="12" height="12"><circle cx="6" cy="6" r="5.5" fill="#fff" stroke="#999"/><path d="M5 3.5 8 6 5 8.5z" fill="#666"/></svg>SHOP</li>
      <li><svg width="12" height="12"><circle cx="6" cy="6" r="5.5" fill="#fff" stroke="#999"/><path d="M5 3.5 8 6 5 8.5z" fill="#666"/></svg>ARTISTS</li>
      <li><svg width="12" height="12"><circle cx="6" cy="6" r="5.5" fill="#fff" stroke="#999"/><path d="M5 3.5 8 6 5 8.5z" fill="#666"/></svg>COMMUNITY</li>
      <li><svg width="12" height="12"><circle cx="6" cy="6" r="5.5" fill="#fff" stroke="#999"/><path d="M5 3.5 8 6 5 8.5z" fill="#666"/></svg>ADD</li>
    </ul>

    <ul class="submenu">
      <li>MAGAZINE</li>
      <li class="is-hover">PICKS</li>
      <li>INTERVIEWS</li>
      <li>CONTRIBUTORS</li>
      <li>ART BLOGROLL</li>
    </ul>

    <h3 class="side-title" style="top:452px">ACTIONS</h3>
    <div class="side-rule" style="top:479px"></div>
    <ul class="actions">
      <li><svg width="16" height="16"><circle cx="8" cy="8" r="7" fill="#5db33a"/><path d="M8 4v8M4 8h8" stroke="#fff" stroke-width="2"/></svg>Add to Mylist</li>
      <li><svg width="16" height="16"><circle cx="8" cy="8" r="7" fill="#5db33a"/><path d="M6 5l5 3-5 3z" fill="#fff"/></svg>View large Slideshow</li>
      <li><svg width="16" height="16"><rect x="0" y="3" width="16" height="11" fill="#f2c200"/><path d="M0 3l8 6 8-6" fill="none" stroke="#c99a00"/></svg>Email this Artist</li>
      <li><svg width="16" height="16"><path d="M8 1 15 14H1z" fill="#f2b600" stroke="#b58400"/><path d="M8 5v5M8 11.5v1.5" stroke="#333" stroke-width="1.6"/></svg>Report Abuse</li>
      <li><svg width="16" height="16"><circle cx="8" cy="8" r="7" fill="#2d7fd0"/><text x="8" y="12" font-size="11" text-anchor="middle" fill="#fff" font-family="Open Sans,sans-serif" font-weight="600">?</text></svg>Contact us for help</li>
      <li><svg width="16" height="16"><rect x="1" y="1" width="14" height="14" rx="2" fill="#2d5f95"/></svg>Bookmark this</li>
      <li><svg width="16" height="16"><rect x="1" y="1" width="14" height="14" rx="2" fill="#4b9a3a"/></svg>Discover it!</li>
      <li><svg width="16" height="16"><rect x="1" y="1" width="14" height="14" rx="2" fill="#3b5998"/></svg>Like it</li>
      <li><svg width="16" height="16"><rect x="1" y="1" width="14" height="14" rx="2" fill="#2fa8e0"/></svg>Post it</li>
    </ul>

    <h3 class="side-title" style="top:793px;left:4px">News &amp; Buzz</h3>
    <div class="side-rule" style="top:819px"></div>
    <ul class="news">
      <li>Upcoming Harbor Fair Special Editions</li>
      <li>Mara Linwood: On Our Worldwide Watchlist</li>
      <li>Watchlist Artist: Tessa Noor</li>
    </ul>
  </aside>

  <header class="topbar">
    <span class="country">Country :</span>
    <div class="select">Worldwide<span class="caret"><svg width="24" height="22"><path d="M6 8h12l-6 7z" fill="#555"/></svg></span></div>
    <span class="userlinks" style="left:530px">Register Free</span>
    <span class="userlinks" style="left:626px">Sign In</span>
    <span class="userlinks" style="left:683px">FAQ</span>
    <ul class="tabs">
      <li class="is-current">PROFILE</li>
      <li>ARTWORKS</li>
      <li>FOR SALE</li>
      <li>NETWORK</li>
      <li>REVIEWS</li>
      <li>COMMENTS</li>
    </ul>
    <span class="search-label">Search :</span>
    <div class="search-box"></div>
  </header>

  <section class="stage">
    <div class="photo" role="img" aria-label="Photograph: woman with dark ponytail and leopard-print earring on a city street"></div>
    <svg class="ctrl" style="left:18px" width="50" height="20"><circle cx="10" cy="10" r="9.5" fill="#fff"/><path d="M12.5 5.5 6.5 10l6 4.5z" fill="#333"/><circle cx="40" cy="10" r="9.5" fill="#fff"/><path d="M40 6 35 10l5 4zM45 6 40 10l5 4z" fill="#333"/></svg>
    <div class="caption">Leopard Earring, 2011</div>
    <svg class="ctrl" style="left:573px" width="50" height="20"><circle cx="10" cy="10" r="9.5" fill="#fff"/><path d="M5 6 10 10l-5 4zM10 6l5 4-5 4z" fill="#333"/><circle cx="40" cy="10" r="9.5" fill="#fff"/><path d="M37.5 5.5 43.5 10l-6 4.5z" fill="#333"/></svg>
  </section>

  <div class="thumbs">
    <div class="thumb" role="img" aria-label="Thumbnail: man with ice cream cone" style="background:linear-gradient(#6b6a60,#2b2a27)"></div>
    <div class="thumb" role="img" aria-label="Thumbnail: woman by stone building" style="background:linear-gradient(#a89b88,#4a3e36)"></div>
    <div class="thumb" role="img" aria-label="Thumbnail: young man in sunglasses" style="background:linear-gradient(#c9c5bf,#3a3330)"></div>
    <div class="thumb" role="img" aria-label="Thumbnail: leopard earring" style="background:linear-gradient(#5a4235,#1f1815)"></div>
    <div class="thumb" role="img" aria-label="Thumbnail: figure in purple scarf" style="background:linear-gradient(#c77f6a,#5b2d5e)"></div>
    <div class="thumb" role="img" aria-label="Thumbnail: man in black hat" style="background:linear-gradient(#d4d2cc,#1f1e1d)"></div>
    <div class="thumb" role="img" aria-label="Thumbnail: young woman outdoors" style="background:linear-gradient(#b8c8d8,#3b2c28)"></div>
  </div>

  <h2 class="section-title" style="top:628px">QUICK FACTS</h2>
  <table class="facts">
    <tr><td class="key">BIRTHPLACE</td><td class="sep">:</td><td>Paris</td></tr>
    <tr><td class="key">BIRTH YEAR</td><td class="sep">:</td><td>1974</td></tr>
    <tr><td class="key">LIVES IN</td><td class="sep">:</td><td>Paris</td></tr>
    <tr><td class="key">WORKS IN</td><td class="sep">:</td><td>Paris</td></tr>
  </table>

  <h2 class="section-title" style="top:788px">STATEMENT</h2>
  <p class="statement">Dorian Pell lives and works in and around Paris. His photography has been shown in all kinds of small galleries, clubs, and alternative arts spaces. He is particularly interested in creating a documentation of people in ordinary, everyday activities, looking for the moments of beauty or magic in the quotidien.</p>

  <footer class="footer">
    <div class="footer-links">CONTACT<span>|</span>ABOUT<span>|</span>ADVERTISE<span>|</span>TERMS<span>|</span>JOIN THE TEAM<span>|</span>FAQ</div>
    <div class="copyright">Copyright © 2006-2012 by MuseQuill, Inc. All images and content remain the © of their rightful owners.</div>
  </footer>

</div>
</body>
</html>
```